Website redesign for a national printing company

Our current website is dated and boring: tidewellflags.com

We are looking for a fresh, modern design. We need a clean, minimal design that is also elegant, really shows off large, bright photos of our banners in action and POPS. Our goal is to showcase our beautiful banners, while also giving the user the confidence in our company that we will provide friendly, fast service, fast printing, and deliver their banners on time for their event.

I want a nice flow to the website, the design should tie in well with the printing feel. Here is an example of clean, beautiful design that ties in to the industry - https://www.vorpa.com/ - notice how the buttons are like chat icons, for example.

More examples:

Nice clean design https://www.brimlet.com/

https://quelmoor.com/ nice and clean, but it POPS really well.

I like https://www.fendrawick.com/

https://www.pruvel.com/ gorgeous site, clean, modern

Beautiful, simple, clean, modern - https://tanvirepay.com/en-us/

These websites are not from the print industry, that’s because most printers don’t have good websites - they are more focused on local businesses, referrals, not really online marketing.

But keep in mind in your design that we need to give the feel that we are printing their banners beautifully, fast, with great service.

https://www.gleamvoxa.com/ so clean, bold, clear to the user what the company does. Love this simple yet elegant design.

https://www.k7.com/ - so pretty! And still so simple and obvious to the user what to do on their site.

https://zelvin.com/

https://marrowfinch.com/us/en/ big and bold - yet super nicely designed with so many nice touches

https://postwrenly.com/ - also clean, simple, and so obvious to the user to take action and contact the company
Updates

I just updated the job brief, and you can also view it in full here - https://files.qorvanet.com/document/d/8Hpz3LRQx-41mTb92nWvJcOaEs-Y67kd0Gf57JuXRTNe/edit?usp=sharing

Target Market(s)

Please read this customer persona - https://files.qorvanet.com/document/d/8Hpz3LRQx-41mTb92nWvJcOaEs-Y67kd0Gf57JuXRTNe/edit?usp=sharing

Industry/Entity Type

Printing

Number of Pages Required

1 page

Requirements
Must have
• Nice flow to the website, the design should tie in well with the printing feel. Here is an example of clean, beautiful design that ties in to the industry - https://www.vorpa.com/ - notice how the buttons are like chat icons, for example.
Should not have
• No filters on the images, we want large, beautiful images.

```html
<!DOCTYPE html>
<html lang="en">
<head>
<meta charset="utf-8">
<title>Tidewell Flags — Large Format Banner Printing</title>
<link href="https://fonts.googleapis.com/css2?family=Poppins:wght@400;500;600;700&family=Open+Sans:wght@400;600&display=swap" rel="stylesheet">
<style>
:root{
  --navy:#070d24;
  --blue:#1446c8;
  --blue-light:#2f66ea;
  --ink:#1a1a1a;
  --muted:#5b5f6b;
  --white:#ffffff;
  --footer:#050505;
  --head:'Poppins',sans-serif;
  --body:'Open Sans',sans-serif;
}
*{margin:0;padding:0;box-sizing:border-box}
html,body{width:1200px;height:3916px;overflow:hidden}
body{font-family:var(--body);color:var(--ink);background:var(--white);position:relative}
section,footer{position:relative;width:1200px;overflow:hidden}
.abs{position:absolute}
.section-title{position:absolute;left:0;width:100%;text-align:center;font-family:var(--head);font-size:34px;font-weight:400;letter-spacing:.5px;text-transform:uppercase}
.section-title b{font-weight:700}
.btn{display:inline-flex;align-items:center;justify-content:center;font-family:var(--head);font-weight:600;font-size:16px;height:44px;padding:0 28px;border-radius:4px;color:var(--white);letter-spacing:.5px;white-space:nowrap}
.btn-blue{background:var(--blue)}
.btn-outline{border:2px solid var(--white)}
.logo{font-family:var(--head);font-weight:700;font-size:28px;color:var(--white);letter-spacing:-.3px;white-space:nowrap}

/* hero */
.hero{height:592px;background:radial-gradient(circle at 70% 40%,#13204f 0%,var(--navy) 65%)}
.nav{position:absolute;top:20px;left:112px;right:112px;height:56px;display:flex;align-items:center}
.nav-links{margin-left:auto;display:flex;gap:26px;align-items:center;font-family:var(--head);font-size:14px;color:var(--white);font-weight:500;white-space:nowrap}
.nav-phone{display:flex;align-items:center;gap:8px}
.nav .btn{margin-left:28px;height:40px;font-size:14px;padding:0 22px}
.hero-title{left:112px;top:168px;font-family:var(--head);font-weight:700;font-size:52px;line-height:64px;color:var(--white)}
.hero-title span{color:var(--blue-light)}
.hero-copy{left:112px;top:326px;width:460px;color:#d6dbea;font-size:16px;line-height:26px}
.hero-actions{left:112px;top:432px;display:flex;gap:22px}
.hero-photo{left:660px;top:168px;width:400px;height:304px;border-radius:14px;background:linear-gradient(135deg,#9fb4d6 0%,#c34a4a 45%,#2c3f8c 100%)}
.dots{left:568px;top:516px;display:flex;gap:12px;align-items:center}
.dots i{width:14px;height:14px;border-radius:50%;background:#7a839c;display:block}
.dots i.on{background:var(--white);width:16px;height:16px;box-shadow:0 0 0 4px rgba(255,255,255,.25)}

/* features */
.features{height:548px;background:var(--white)}
.features .section-title{top:82px}
.feature-row{position:absolute;top:152px;left:92px;width:1016px;display:flex;justify-content:space-between}
.feature{width:240px;height:310px;text-align:center;padding-top:32px;border-radius:6px}
.feature.active{background:var(--white);box-shadow:0 10px 40px rgba(10,20,60,.18);margin-top:-24px;padding-top:40px}
.feature-icon{width:110px;height:110px;margin:0 auto;display:flex;align-items:center;justify-content:center}
.feature.active .feature-icon{background:var(--blue);border-radius:50%;box-shadow:0 0 0 8px rgba(20,70,200,.15)}
.feature h3{font-family:var(--head);font-size:22px;font-weight:600;margin-top:16px}
.feature p{font-size:14px;line-height:22px;color:var(--muted);margin:16px auto 0;width:200px}
.feature .go{width:24px;height:24px;border-radius:50%;background:var(--blue);margin:18px auto 0;display:flex;align-items:center;justify-content:center}

/* about */
.about{height:512px;background:linear-gradient(90deg,#0b1433 0%,var(--navy) 100%)}
.about-ring{left:200px;top:76px;width:360px;height:360px;border-radius:50%;border:8px solid var(--blue);padding:10px}
.about-photo{width:100%;height:100%;border-radius:50%;background:linear-gradient(160deg,#6f88b8 0%,#2b3a6b 55%,#b2403c 100%)}
.about-title{left:640px;top:128px;font-family:var(--head);font-size:34px;color:var(--white);font-weight:400}
.about-title b{font-weight:700}
.about-copy{left:640px;top:196px;width:460px;color:#d6dbea;font-size:16px;line-height:26px}
.about .btn{position:absolute;left:640px;top:340px}

/* process */
.process{height:468px;background:var(--white)}
.process .section-title{top:80px}
.step{position:absolute;top:188px;width:240px;text-align:center}
.step-circle{width:136px;height:136px;margin:0 auto;border-radius:50%;background:var(--blue);box-shadow:0 0 0 10px rgba(20,70,200,.15);display:flex;align-items:center;justify-content:center}
.step h3{font-family:var(--head);font-size:22px;font-weight:600;margin-top:48px}
.step-arrow{position:absolute;top:250px}

/* testimonials */
.testimonials{height:640px;background:linear-gradient(180deg,#e3e6ec 0%,#f3f4f7 50%,#dfe3ea 100%)}
.testimonials .section-title{top:82px}
.quote{position:absolute;top:156px;width:460px;min-height:72px}
.quote-mark{width:72px;height:72px;border-radius:50%;background:var(--blue);display:flex;align-items:center;justify-content:center;position:absolute;left:0;top:0}
.quote p{margin-left:92px;padding-top:6px;font-size:15px;line-height:24px;color:#333}
.reviewer{position:absolute;top:384px;display:flex;align-items:center;gap:18px}
.avatar{width:80px;height:80px;border-radius:50%;background:linear-gradient(135deg,#c9a789,#6a7a93);border:4px solid var(--white)}
.stars{color:var(--blue);font-size:16px;letter-spacing:2px}
.name{font-family:var(--head);font-size:16px;color:var(--blue);font-weight:500}
.slider-nav{left:564px;top:488px;display:flex;gap:8px}
.slider-nav span{width:28px;height:28px;border-radius:50%;background:var(--navy);display:flex;align-items:center;justify-content:center}
.slider-nav span.on{background:var(--blue)}

/* gallery */
.gallery{height:760px;background:var(--white)}
.gallery .section-title{top:40px}
.tile{position:absolute}
.t1{left:112px;top:108px;width:388px;height:604px;background:linear-gradient(170deg,#a7c4df 0%,#d9c7cf 45%,#6c5a4c 100%)}
.t2{left:524px;top:108px;width:268px;height:272px;background:linear-gradient(160deg,#26408e 0%,#3c5fb8 50%,#1a2b60 100%)}
.t3{left:816px;top:108px;width:268px;height:272px;background:linear-gradient(160deg,#2a2a33 0%,#8c6f55 55%,#d8d1c6 100%)}
.t4{left:524px;top:400px;width:268px;height:312px;background:linear-gradient(170deg,#8bb6d9 0%,#e8e8e8 45%,#3c4a3a 100%)}
.t5{left:816px;top:400px;width:268px;height:312px;background:linear-gradient(170deg,#a9c3d9 0%,#f0f0f0 40%,#b24a3a 100%)}

/* footer */
.site-footer{height:396px;background:var(--footer);color:var(--white)}
.footer-brand{left:112px;top:104px}
.socials{left:112px;top:164px;display:flex;gap:14px}
.socials i{width:40px;height:40px;border-radius:50%;background:var(--white);display:block}
.footer-col{top:96px}
.footer-col h4{font-family:var(--head);font-size:17px;font-weight:600;margin-bottom:22px;letter-spacing:.5px}
.footer-col li{list-style:none;font-size:15px;line-height:24px;color:#e4e4e4}
.contact-line{display:flex;gap:12px;align-items:flex-start;font-size:15px;line-height:24px;margin-bottom:14px;color:#e4e4e4}
.newsletter{display:flex;margin-top:2px}
.newsletter span{width:180px;height:40px;background:var(--white);color:#888;font-size:14px;padding:10px 12px}
.newsletter b{width:40px;height:40px;background:var(--blue);display:flex;align-items:center;justify-content:center}
.footer-rule{left:112px;right:112px;top:320px;height:1px;background:#2a2a2a}
.copyright{left:0;width:100%;top:336px;text-align:center;font-size:15px;color:#e4e4e4}
</style>
</head>
<body>

<section class="hero">
  <svg class="abs" style="left:0;top:0" width="1200" height="592" aria-hidden="true">
    <g fill="none" stroke="#ffffff" stroke-width="6" opacity=".9">
      <path d="M800 210a60 60 0 0 1 60-60"/><path d="M782 210a78 78 0 0 1 78-78"/>
      <path d="M1000 540a60 60 0 0 0 60-60"/><path d="M1000 558a78 78 0 0 0 78-78"/>
    </g>
    <g stroke="#ffffff" stroke-width="6" stroke-linecap="round">
      <path d="M582 102l16 16M598 102l-16 16"/>
      <path d="M630 286v14M623 293h14"/>
      <path d="M1052 548v14M1045 555h14"/>
    </g>
  </svg>
  <nav class="nav">
    <div class="logo">Tidewell Flags</div>
    <div class="nav-links">
      <span>Home</span><span>About</span><span>Products</span><span>Gallery</span><span>Contact</span>
      <span class="nav-phone">
        <svg width="15" height="15" viewBox="0 0 24 24" fill="#fff" aria-hidden="true"><path d="M6.6 10.8a15.1 15.1 0 0 0 6.6 6.6l2.2-2.2a1 1 0 0 1 1-.25 11.4 11.4 0 0 0 3.6.57 1 1 0 0 1 1 1V20a1 1 0 0 1-1 1A17 17 0 0 1 3 4a1 1 0 0 1 1-1h3.5a1 1 0 0 1 1 1c0 1.25.2 2.45.57 3.57a1 1 0 0 1-.25 1z"/></svg>
        800-555-0142
      </span>
    </div>
    <span class="btn btn-blue">GET A QUOTE</span>
  </nav>
  <h1 class="abs hero-title">LARGE FORMAT<br><span>BANNER</span> PRINTING</h1>
  <p class="abs hero-copy">As a banner printer for thousands of events across the US, our sales team understands when you're hustling to meet a tight deadline for an event.</p>
  <div class="abs hero-actions">
    <span class="btn btn-outline">UPLOAD</span>
    <span class="btn btn-blue">CONTACT</span>
  </div>
  <div class="abs hero-photo" role="img" aria-label="Photo of large printed banners hung around an outdoor event stage"></div>
  <div class="abs dots"><i></i><i class="on"></i><i></i></div>
</section>

<section class="features">
  <h2 class="section-title"><b>WHY</b> CHOOSE US</h2>
  <div class="feature-row">
    <div class="feature">
      <div class="feature-icon">
        <svg width="64" height="64" viewBox="0 0 64 64" fill="none" stroke="#1446c8" stroke-width="3" stroke-linejoin="round" aria-hidden="true"><path d="M20 56V28h-10v28zM20 30l12-22c4 0 6 3 5 7l-2 9h16c3 0 5 3 4 6l-5 18c-1 3-3 4-6 4H20"/></svg>
      </div>
      <h3>Friendly</h3>
      <p>Lorem ipsum dolor sit amet, consectetur adipiscing elit, sed do eiusmod tempor</p>
      <div class="go"><svg width="10" height="10" viewBox="0 0 10 10" aria-hidden="true"><path d="M3 1l4 4-4 4" stroke="#fff" stroke-width="2" fill="none"/></svg></div>
    </div>
    <div class="feature active">
      <div class="feature-icon">
        <svg width="60" height="60" viewBox="0 0 64 64" fill="none" stroke="#fff" stroke-width="3.5" stroke-linecap="round" aria-hidden="true"><circle cx="32" cy="36" r="22"/><path d="M32 36V22M26 8h12M32 8v6M50 16l4-4"/></svg>
      </div>
      <h3>Fast Service</h3>
      <p>Lorem ipsum dolor sit amet, consectetur adipiscing elit, sed do eiusmod tempor</p>
      <div class="go"><svg width="10" height="10" viewBox="0 0 10 10" aria-hidden="true"><path d="M3 1l4 4-4 4" stroke="#fff" stroke-width="2" fill="none"/></svg></div>
    </div>
    <div class="feature">
      <div class="feature-icon">
        <svg width="64" height="64" viewBox="0 0 64 64" fill="none" stroke="#1446c8" stroke-width="3" stroke-linejoin="round" aria-hidden="true"><path d="M18 22V8h28v14M18 46H8V22h48v24H46"/><path d="M18 36h28v22H18z"/><path d="M24 44h16M24 50h12"/></svg>
      </div>
      <h3>Fast Printing</h3>
      <p>Lorem ipsum dolor sit amet, consectetur adipiscing elit, sed do eiusmod tempor</p>
      <div class="go"><svg width="10" height="10" viewBox="0 0 10 10" aria-hidden="true"><path d="M3 1l4 4-4 4" stroke="#fff" stroke-width="2" fill="none"/></svg></div>
    </div>
    <div class="feature">
      <div class="feature-icon">
        <svg width="70" height="64" viewBox="0 0 70 64" fill="none" stroke="#1446c8" stroke-width="3" stroke-linejoin="round" aria-hidden="true"><path d="M4 16h38v30H4zM42 26h14l10 10v10H42z"/><circle cx="16" cy="48" r="6" fill="#fff"/><circle cx="54" cy="48" r="6" fill="#fff"/></svg>
      </div>
      <h3>Delivery</h3>
      <p>Lorem ipsum dolor sit amet, consectetur adipiscing elit, sed do eiusmod tempor</p>
      <div class="go"><svg width="10" height="10" viewBox="0 0 10 10" aria-hidden="true"><path d="M3 1l4 4-4 4" stroke="#fff" stroke-width="2" fill="none"/></svg></div>
    </div>
  </div>
</section>

<section class="about">
  <div class="abs about-ring"><div class="about-photo" role="img" aria-label="Photo of an outdoor stage wrapped in a large printed backdrop banner"></div></div>
  <h2 class="abs about-title"><b>ABOUT</b> US</h2>
  <p class="abs about-copy">For over two decades, Tidewell Flags has been the go-to source for high-quality custom printing for large format banners, plastic roll banners, stage backdrops and mobile stage festival banners.</p>
  <span class="btn btn-blue">GET A QUOTE</span>
</section>

<section class="process">
  <h2 class="section-title"><b>OUR</b> PROCESS</h2>
  <div class="step" style="left:148px">
    <div class="step-circle">
      <svg width="60" height="56" viewBox="0 0 60 56" fill="none" stroke="#fff" stroke-width="3" aria-hidden="true"><rect x="4" y="4" width="52" height="40" rx="3"/><path d="M4 14h52M20 52h20M30 44v8"/><circle cx="10" cy="9" r="1.5" fill="#fff"/><path d="M14 24h32M14 32h20"/></svg>
    </div>
    <h3>Booking</h3>
  </div>
  <svg class="step-arrow" style="left:394px" width="90" height="20" viewBox="0 0 90 20" aria-hidden="true"><path d="M2 14c30-12 56-12 84-2m-8-6l8 6-9 4" fill="none" stroke="#777" stroke-width="2"/></svg>
  <div class="step" style="left:472px">
    <div class="step-circle">
      <svg width="60" height="60" viewBox="0 0 60 60" fill="none" stroke="#fff" stroke-width="3" stroke-linecap="round" aria-hidden="true"><path d="M10 50L46 14M40 8l12 12M12 12l12 12M8 16l8-8M36 36l12 12M44 32l-12 12"/></svg>
    </div>
    <h3>Select Design</h3>
  </div>
  <svg class="step-arrow" style="left:720px" width="90" height="20" viewBox="0 0 90 20" aria-hidden="true"><path d="M2 14c30-12 56-12 84-2m-8-6l8 6-9 4" fill="none" stroke="#777" stroke-width="2"/></svg>
  <div class="step" style="left:812px">
    <div class="step-circle">
      <svg width="60" height="60" viewBox="0 0 60 60" fill="none" stroke="#fff" stroke-width="3" stroke-linejoin="round" aria-hidden="true"><rect x="10" y="8" width="40" height="44" rx="3"/><path d="M16 42l10-12 8 8 6-6 6 10z"/><circle cx="38" cy="20" r="4"/></svg>
    </div>
    <h3>Start Printing</h3>
  </div>
</section>

<section class="testimonials" role="img" aria-label="Faded background photo of a crowd in front of event banners">
  <h2 class="section-title"><b>OUR</b> TESTIMONIALS</h2>
  <div class="quote" style="left:132px">
    <div class="quote-mark"><svg width="32" height="26" viewBox="0 0 32 26" fill="#fff" aria-hidden="true"><path d="M0 26V14C0 6 4 1 12 0v5c-4 1-6 4-6 8h6v13zM18 26V14c0-8 4-13 12-14v5c-4 1-6 4-6 8h6v13z"/></svg></div>
    <p>The banner turned out great and was delivered promptly. Looks great at gigs. Jo Pell, Rusty Vane and the Tin Owls</p>
  </div>
  <div class="quote" style="left:652px">
    <div class="quote-mark"><svg width="32" height="26" viewBox="0 0 32 26" fill="#fff" aria-hidden="true"><path d="M0 26V14C0 6 4 1 12 0v5c-4 1-6 4-6 8h6v13zM18 26V14c0-8 4-13 12-14v5c-4 1-6 4-6 8h6v13z"/></svg></div>
    <p>Marcus and the team at Tidewell Flags have been great to work with. Their eye to detail is spot on. Don't be afraid to ask as many questions as you like. Fast shipping and wonderful quality product! Will be using them again soon.</p>
  </div>
  <div class="reviewer" style="left:172px">
    <div class="avatar" role="img" aria-label="Customer portrait photo"></div>
    <div><div class="stars">★★★★★</div><div class="name">– Dana Whitlow</div></div>
  </div>
  <div class="reviewer" style="left:708px">
    <div class="avatar" role="img" aria-label="Customer portrait photo"></div>
    <div><div class="stars">★★★★★</div><div class="name">– Marcus Fennel</div></div>
  </div>
  <div class="abs slider-nav">
    <span><svg width="10" height="10" viewBox="0 0 10 10" aria-hidden="true"><path d="M7 1L3 5l4 4" stroke="#fff" stroke-width="2" fill="none"/></svg></span>
    <span class="on"><svg width="10" height="10" viewBox="0 0 10 10" aria-hidden="true"><path d="M3 1l4 4-4 4" stroke="#fff" stroke-width="2" fill="none"/></svg></span>
  </div>
</section>

<section class="gallery">
  <h2 class="section-title"><b>OUR</b> GALLERY</h2>
  <div class="tile t1" role="img" aria-label="Photo of a child beside a playhouse decorated with a printed wish banner"></div>
  <div class="tile t2" role="img" aria-label="Photo of a large blue printed banner on display"></div>
  <div class="tile t3" role="img" aria-label="Photo of a crowded indoor event with printed banners"></div>
  <div class="tile t4" role="img" aria-label="Photo of a football academy banner on a stadium fence"></div>
  <div class="tile t5" role="img" aria-label="Photo of sponsor banners along a running track"></div>
</section>

<footer class="site-footer">
  <div class="abs logo footer-brand">Tidewell Flags</div>
  <div class="abs socials"><i></i><i></i><i></i></div>
  <div class="abs footer-col" style="left:380px">
    <h4>QUICK LINKS</h4>
    <ul><li>Home</li><li>About</li><li>Product</li><li>Contact Us</li></ul>
  </div>
  <div class="abs footer-col" style="left:572px">
    <h4>CONTACT US</h4>
    <div class="contact-line"><svg width="16" height="20" viewBox="0 0 16 20" fill="#fff" aria-hidden="true"><path d="M8 0a8 8 0 0 0-8 8c0 6 8 12 8 12s8-6 8-12a8 8 0 0 0-8-8zm0 11a3 3 0 1 1 0-6 3 3 0 0 1 0 6z"/></svg><span>Lorem ipsum dolor<br>sit amet, consectetur</span></div>
    <div class="contact-line"><svg width="16" height="16" viewBox="0 0 24 24" fill="#fff" aria-hidden="true"><path d="M6.6 10.8a15.1 15.1 0 0 0 6.6 6.6l2.2-2.2a1 1 0 0 1 1-.25 11.4 11.4 0 0 0 3.6.57 1 1 0 0 1 1 1V20a1 1 0 0 1-1 1A17 17 0 0 1 3 4a1 1 0 0 1 1-1h3.5a1 1 0 0 1 1 1c0 1.25.2 2.45.57 3.57a1 1 0 0 1-.25 1z"/></svg><span>800-555-0142</span></div>
    <div class="contact-line"><svg width="16" height="14" viewBox="0 0 20 14" aria-hidden="true"><rect x="1" y="1" width="18" height="12" fill="none" stroke="#fff" stroke-width="2"/><path d="M1 1l9 7 9-7" fill="none" stroke="#fff" stroke-width="2"/></svg><span>info@tidewellflags.com</span></div>
  </div>
  <div class="abs footer-col" style="left:860px">
    <h4>NEWSLETTER</h4>
    <div class="newsletter"><span>Enter email</span><b><svg width="16" height="14" viewBox="0 0 20 14" aria-hidden="true"><rect x="1" y="1" width="18" height="12" fill="none" stroke="#fff" stroke-width="2"/><path d="M1 1l9 7 9-7" fill="none" stroke="#fff" stroke-width="2"/></svg></b></div>
  </div>
  <div class="abs footer-rule"></div>
  <p class="abs copyright">©Copyrights 2023 Tidewell Flags &nbsp;|&nbsp; All Rights Reserved.</p>
</footer>

</body>
</html>
```